help me Create Brightfern Catering offsite menus

I need something vibrant and it needs some pictures to go with the food i will include the logo of the location and the menu. it is for offsite catering to be delivered to venues in our local town, we are currently catering in house only but are expanding to do delivery so need something that i can use as a menu. the file needs to be able to be edited

Target Market(s)

local small businesses that require catering for their group lunches

Industry/Entity Type

Catering

Font styles to use
Serif
Decorative

Requirements
Must have
• colour and soul, must have a good feeling and be happy
Nice to have
• some other stock photos of the described products
Should not have
• not be too corporate and businessy

```html
<!DOCTYPE html>
<html lang="en">
<head>
<meta charset="utf-8">
<title>Brightfern Catering – Offsite Menu</title>
<link href="https://fonts.googleapis.com/css2?family=Almendra:wght@400;700&family=Amatic+SC:wght@700&family=Lato:wght@400&display=swap" rel="stylesheet">
<style>
  :root{
    --backdrop:#e9e4dc;
    --page:#101a24;
    --page-edge:#1d2833;
    --ink:#ece8e0;
    --ink-soft:#b9b4ab;
    --ribbon:#a97b47;
    --ribbon-ink:#fff6e6;
    --badge:#12324d;
    --swirl-gold:rgba(169,123,71,.28);
    --swirl-silver:rgba(200,200,200,.22);
    --photo-top:#6f7e86;
    --photo-bottom:#9a7a52;
  }
  *{box-sizing:border-box;margin:0;padding:0}
  html,body{width:1200px;height:754px;overflow:hidden;background:var(--backdrop)}
  .canvas{position:relative;width:1200px;height:754px}
  .menu-page{
    position:absolute;top:17px;width:556px;height:720px;background:var(--page);
    clip-path:polygon(20px 0,calc(100% - 20px) 0,100% 20px,100% calc(100% - 20px),calc(100% - 20px) 100%,20px 100%,0 calc(100% - 20px),0 20px);
  }
  .menu-page::before{
    content:"";position:absolute;inset:8px;border:1px solid var(--page-edge);
    clip-path:polygon(16px 0,calc(100% - 16px) 0,100% 16px,100% calc(100% - 16px),calc(100% - 16px) 100%,16px 100%,0 calc(100% - 16px),0 16px);
  }
  .page-left{left:32px}
  .page-right{left:612px}
  .abs{position:absolute}
  .ornament{position:absolute;border-radius:50%}
  .ornament.gold{background:radial-gradient(closest-side,var(--swirl-gold),transparent)}
  .ornament.silver{background:radial-gradient(closest-side,var(--swirl-silver),transparent)}
  .brand-badge{
    position:absolute;border-radius:50%;background:var(--badge);
    display:flex;align-items:center;justify-content:center;gap:6px;
    font-family:"Almendra",serif;font-weight:700;color:var(--ink);text-align:center;line-height:1.05;
  }
  .brand-dot{border-radius:50%;background:var(--ribbon);flex:none}
  .ribbon{
    position:absolute;height:25px;background:var(--ribbon);color:var(--ribbon-ink);
    font-family:"Almendra",serif;font-weight:700;font-size:15px;letter-spacing:.5px;
    display:flex;align-items:center;justify-content:center;
    clip-path:polygon(0 0,100% 0,96% 50%,100% 100%,0 100%,4% 50%);
  }
  .ribbon.large{height:32px;font-size:19px}
  .menu-line{
    position:absolute;display:flex;justify-content:space-between;
    font-family:"Amatic SC",sans-serif;font-weight:700;color:var(--ink);font-size:15px;letter-spacing:.4px;line-height:1;
  }
  .menu-note{display:block;font-size:10px;color:var(--ink-soft);margin-top:3px}
  .rule{position:absolute;width:1.5px;background:var(--ink)}
  .venue-photo{
    position:absolute;left:295px;top:213px;width:178px;height:174px;
    background:linear-gradient(180deg,var(--photo-top) 0%,#4e5a61 55%,var(--photo-bottom) 100%);
  }
  .lunch-copy{
    position:absolute;left:205px;top:609px;width:300px;text-align:center;
    font-family:"Almendra",serif;font-weight:700;font-size:10.5px;color:var(--ink);line-height:1.45;
  }
  .phone{
    position:absolute;right:36px;top:652px;display:flex;align-items:center;gap:8px;
    font-family:"Lato",sans-serif;font-size:15px;color:var(--ink);
  }
  .footer-note{position:absolute;left:160px;top:676px;font-family:"Lato",sans-serif;font-size:8.5px;color:var(--ink)}
</style>
</head>
<body>
<main class="canvas">

  <!-- Left page -->
  <section class="menu-page page-left">
    <div class="ornament gold" style="left:247px;top:30px;width:215px;height:150px" role="img" aria-label="Curling gold flourish ornament"></div>
    <div class="ornament gold" style="left:480px;top:320px;width:62px;height:52px" role="img" aria-label="Small gold flourish ornament"></div>
    <div class="ornament gold" style="left:22px;top:490px;width:82px;height:105px" role="img" aria-label="Gold swirl ornament"></div>
    <div class="ornament gold" style="left:390px;top:600px;width:160px;height:110px" role="img" aria-label="Gold swirl ornament"></div>

    <div class="brand-badge" style="left:56px;top:26px;width:176px;height:176px;font-size:24px">
      <span>Brightfern<br>Catering</span><span class="brand-dot" style="width:12px;height:12px"></span>
    </div>

    <div class="ribbon" style="left:64px;top:217px;width:192px">Tea &amp; Coffee</div>
    <div class="menu-line" style="left:84px;top:262px;width:160px;font-size:12px">
      <span>Tea and coffee station<span class="menu-note" style="font-size:7px">Continuous tea and coffee served through the day</span></span><span>$3.00pp</span>
    </div>
    <div class="menu-line" style="left:84px;top:288px;width:160px;font-size:12px">
      <span>Barrista delivered<span class="menu-note" style="font-size:7px">(pre order only)</span></span><span>$5.50 each</span>
    </div>
    <div class="rule" style="left:259px;top:261px;height:36px"></div>

    <div class="ribbon" style="left:64px;top:331px;width:192px">Extra</div>
    <div class="menu-line" style="left:84px;top:374px;width:160px;font-size:12px">
      <span>Juice 2 lt bottle</span><span>$3.95</span>
    </div>
    <div class="rule" style="left:259px;top:374px;height:10px"></div>

    <div class="venue-photo" role="img" aria-label="Photo of a catering platter on a table in a bright venue with large windows"></div>

    <div class="ribbon" style="left:86px;top:416px;width:384px">Morning or afternoon Tea</div>

    <div class="menu-line" style="left:138px;top:468px;width:290px"><span>Scones and slices platter</span><span style="width:90px">$6.50 per person</span></div>
    <div class="menu-line" style="left:138px;top:495px;width:290px"><span>Muffins</span><span style="width:90px">$5.00 per person</span></div>
    <div class="menu-line" style="left:138px;top:525px;width:290px"><span>Homemade biscuits</span><span style="width:90px">$4.50 per person</span></div>
    <div class="menu-line" style="left:138px;top:552px;width:290px"><span>Banana bread</span><span style="width:90px">$6.00 per person</span></div>
    <div class="menu-line" style="left:138px;top:585px;width:290px"><span>Gluten free frittata</span><span style="width:90px">$5.50 per person</span></div>
    <div class="menu-line" style="left:138px;top:611px;width:290px"><span>Ploughmans platter</span><span style="width:90px">$8.50 per person</span></div>
    <div class="menu-line" style="left:138px;top:642px;width:290px"><span>Whole fresh fruit platter</span><span style="width:90px">$45.00 per platter</span></div>
    <div class="menu-line" style="left:138px;top:669px;width:290px"><span>Chopped fresh seasonal fruit platter</span><span style="width:90px">$49.50 per platter</span></div>
    <div class="rule" style="left:438px;top:466px;height:216px"></div>
  </section>

  <!-- Right page -->
  <section class="menu-page page-right">
    <div class="ornament silver" style="left:14px;top:10px;width:405px;height:125px" role="img" aria-label="Silver flowing flourish ornament"></div>
    <div class="ornament silver" style="left:28px;top:500px;width:145px;height:190px" role="img" aria-label="Large silver swirl ornament"></div>

    <div class="brand-badge" style="left:466px;top:46px;width:68px;height:68px;font-size:10px;gap:3px">
      <span>Brightfern<br>Catering</span><span class="brand-dot" style="width:6px;height:6px"></span>
    </div>

    <div class="ribbon large" style="left:47px;top:144px;width:474px">Platter menu</div>

    <div class="menu-line" style="left:69px;top:198px;width:411px;font-size:13px"><span>Hot finger food platter (chef's choice 60 pieces)</span><span>$105.00</span></div>
    <div class="menu-line" style="left:69px;top:223px;width:411px;font-size:13px"><span>Hot roast buffet platter pork or beef with roast vegetables<span class="menu-note">&amp; one grazing salad minimum 10 guests</span></span><span>$16.50pp</span></div>
    <div class="menu-line" style="left:69px;top:264px;width:411px;font-size:13px"><span>Sandwich box (10 rounds)</span><span>$68.00</span></div>
    <div class="menu-line" style="left:69px;top:289px;width:411px;font-size:13px"><span>Medium bread roll platter 15 medium size lunch rolls</span><span>$75.00</span></div>
    <div class="menu-line" style="left:69px;top:315px;width:411px;font-size:13px"><span>Large meat and salad rolls<span class="menu-note">(choice of chicken, chicken schnitzel, roast beef, ham)</span></span><span>$9.00 each</span></div>
    <div class="menu-line" style="left:69px;top:356px;width:411px;font-size:13px"><span>Wraps<span class="menu-note">(choice of chicken, chicken schnitzel, roast beef, ham)</span></span><span>$7.50 each</span></div>
    <div class="menu-line" style="left:69px;top:397px;width:411px;font-size:13px"><span>Individual salad bowls – caesar, greek, creamy pasta, seafood<span class="menu-note">add chicken or grilled chicken schnitzel</span></span><span>$9.50<span class="menu-note">$3.50</span></span></div>
    <div class="menu-line" style="left:69px;top:441px;width:411px;font-size:13px"><span>Large grazing salads – add one to a sandwich platter<span class="menu-note">or hot finger food platter add a healthy side for your group (serves 10)</span></span><span>$35.00</span></div>
    <div class="menu-line" style="left:69px;top:482px;width:411px;font-size:13px"><span>Pizza, pasta and salad (minimum 8 guests)</span><span>$19.00pp</span></div>
    <div class="rule" style="left:497px;top:198px;height:298px"></div>

    <div class="ribbon large" style="left:200px;top:531px;width:305px">Lunch</div>
    <div class="menu-line" style="left:227px;top:582px;width:245px;font-size:17px"><span>Gazing table minimum 5</span><span>$16.50 pp</span></div>
    <p class="lunch-copy">Make your own sandwich buffet for guests to make their own sandwich from a variety of breads and fillings with tea and coffee facilities.</p>

    <div class="phone">
      <svg width="13" height="13" viewBox="0 0 24 24" aria-hidden="true"><circle cx="12" cy="12" r="10.5" fill="none" stroke="#b9b4ab" stroke-width="1.5"/><path d="M9 7l2 3-1.2 1.2a7 7 0 0 0 3 3L14 13l3 2-1 2c-4 0-8.5-4.5-8.5-8.5z" fill="#b9b4ab"/></svg>
      <span>69 555 018</span>
    </div>
    <p class="footer-note">To book in your event call us Now on 69 555 018 or go to www.brightferncatering.com.au</p>
  </section>

</main>
</body>
</html>
```